App Design for quiz app (casual gaming app)

We need an design & logo for our quiz app. Its a simple quiz app, where you pick up a category, answer three questions out of this category. After this an opponent is assigned to your game, and has to answer the same three questions. After this first round is finished, it's the opponents turn to choose a new category and answer three questions out of this category. Now it's your turn to answer the same three questions. With this done, the 2nd round is finished. One game has seven rounds.
Please find attached the balsamiq project. For all of you, do not have balsamiq, please find also the mockups as pdf.
Final delivery should be psd files
Target Market(s)
Casual Games

```html
<!DOCTYPE html>
<html lang="en">
<head>
<meta charset="utf-8">
<title>Quiz Game – Finished</title>
<link href="https://fonts.googleapis.com/css2?family=Open+Sans:wght@400;600;700&display=swap" rel="stylesheet">
<style>
  :root {
    --backdrop: #ecebe8;
    --brand-orange: #ffb600;
    --row-orange: #fbc043;
    --screen-white: #ffffff;
    --ink: #1e1e1e;
    --label-white: #ffffff;
    --wrong-red: #e0443a;
    --right-green: #2fd57a;
    --open-white: #ffffff;
    --avatar-teal: #3aa9a0;
    --avatar-yellow: #f6c534;
  }
  * { box-sizing: border-box; margin: 0; padding: 0; }
  html, body { width: 1200px; height: 789px; overflow: hidden; }
  body {
    background: var(--backdrop);
    font-family: "Open Sans", Arial, sans-serif;
    display: flex;
    justify-content: center;
    align-items: center;
  }
  .app-screen {
    width: 420px;
    height: 760px;
    background: var(--screen-white);
    overflow: hidden;
    display: flex;
    flex-direction: column;
  }
  .status-bar {
    height: 22px;
    background: var(--brand-orange);
    color: var(--label-white);
    font-size: 12px;
    display: flex;
    align-items: center;
    justify-content: space-between;
    padding: 0 8px;
  }
  .status-bar .carrier, .status-bar .battery { display: flex; align-items: center; gap: 5px; }
  .status-bar .time { font-weight: 600; }
  .nav-bar {
    height: 42px;
    background: var(--brand-orange);
    color: var(--label-white);
    font-size: 18px;
    font-weight: 400;
    display: flex;
    align-items: center;
    justify-content: center;
  }
  .match-header {
    height: 118px;
    position: relative;
  }
  .player {
    position: absolute;
    display: flex;
    flex-direction: column;
    align-items: center;
    gap: 4px;
    font-size: 15px;
    font-weight: 600;
    color: var(--ink);
  }
  .player--one { left: 26px; top: 10px; }
  .player--two { right: 26px; top: 26px; }
  .avatar { width: 72px; height: 72px; border-radius: 50%; }
  .avatar--one { background: var(--avatar-teal); }
  .avatar--two { background: var(--avatar-yellow); }
  .score {
    position: absolute;
    left: 0; right: 0; top: 34px;
    text-align: center;
    font-size: 40px;
    font-weight: 600;
    letter-spacing: 2px;
    color: var(--ink);
  }
  .rounds {
    list-style: none;
    display: flex;
    flex-direction: column;
    gap: 10px;
    padding: 0 10px 12px;
  }
  .round {
    height: 84px;
    background: var(--row-orange);
    border-radius: 6px;
    display: flex;
    align-items: center;
    justify-content: space-between;
    padding: 0 16px;
  }
  .round-title {
    text-align: center;
    color: var(--label-white);
    font-weight: 700;
    font-size: 17px;
    line-height: 1.25;
    letter-spacing: 1px;
  }
  .round-title .category { display: block; font-weight: 600; letter-spacing: 0.5px; }
  .answers { display: flex; gap: 9px; }
  .answer { width: 25px; height: 25px; }
  .answer--wrong { background: var(--wrong-red); }
  .answer--right { background: var(--right-green); }
  .answer--open { background: var(--open-white); }
</style>
</head>
<body>
  <main class="app-screen">
    <div class="status-bar">
      <span class="carrier">●●●○○ ABC
        <svg width="13" height="10" viewBox="0 0 13 10" aria-hidden="true"><path d="M1 3.5a8 8 0 0 1 11 0M3 5.8a5 5 0 0 1 7 0M5 8a2 2 0 0 1 3 0" fill="none" stroke="#fff" stroke-width="1.4"/></svg>
      </span>
      <span class="time">4:21 PM</span>
      <span class="battery">22%
        <svg width="24" height="11" viewBox="0 0 24 11" aria-hidden="true"><rect x="0.5" y="0.5" width="20" height="10" rx="2" fill="none" stroke="#fff"/><rect x="2" y="2" width="4" height="7" fill="#fff"/><rect x="21.5" y="3.5" width="2" height="4" fill="#fff"/></svg>
      </span>
    </div>
    <header class="nav-bar">Finished</header>

    <section class="match-header">
      <div class="player player--one">
        <div class="avatar avatar--one" role="img" aria-label="Player 1 avatar: cartoon boy on teal circle"></div>
        <span>Player 1</span>
      </div>
      <div class="score">15:30</div>
      <div class="player player--two">
        <div class="avatar avatar--two" role="img" aria-label="Player 2 avatar: cartoon girl on yellow circle"></div>
        <span>Player 2</span>
      </div>
    </section>

    <ol class="rounds">
      <li class="round">
        <div class="answers"><span class="answer answer--wrong"></span><span class="answer answer--wrong"></span><span class="answer answer--right"></span></div>
        <div class="round-title">ROUND 1<span class="category">Category</span></div>
        <div class="answers"><span class="answer answer--wrong"></span><span class="answer answer--right"></span><span class="answer answer--right"></span></div>
      </li>
      <li class="round">
        <div class="answers"><span class="answer answer--wrong"></span><span class="answer answer--wrong"></span><span class="answer answer--right"></span></div>
        <div class="round-title">ROUND 2<span class="category">Category</span></div>
        <div class="answers"><span class="answer answer--right"></span><span class="answer answer--wrong"></span><span class="answer answer--wrong"></span></div>
      </li>
      <li class="round">
        <div class="answers"><span class="answer answer--wrong"></span><span class="answer answer--wrong"></span><span class="answer answer--right"></span></div>
        <div class="round-title">ROUND 3<span class="category">Category</span></div>
        <div class="answers"><span class="answer answer--right"></span><span class="answer answer--wrong"></span><span class="answer answer--wrong"></span></div>
      </li>
      <li class="round">
        <div class="answers"><span class="answer answer--wrong"></span><span class="answer answer--wrong"></span><span class="answer answer--wrong"></span></div>
        <div class="round-title">ROUND 4<span class="category">Category</span></div>
        <div class="answers"><span class="answer answer--right"></span><span class="answer answer--right"></span><span class="answer answer--right"></span></div>
      </li>
      <li class="round">
        <div class="answers"><span class="answer answer--open"></span><span class="answer answer--open"></span><span class="answer answer--open"></span></div>
        <div class="round-title">ROUND 5<span class="category">Category</span></div>
        <div class="answers"><span class="answer answer--open"></span><span class="answer answer--open"></span><span class="answer answer--open"></span></div>
      </li>
      <li class="round">
        <div class="answers"><span class="answer answer--open"></span><span class="answer answer--open"></span><span class="answer answer--open"></span></div>
        <div class="round-title">ROUND 6<span class="category">Category</span></div>
        <div class="answers"><span class="answer answer--open"></span><span class="answer answer--open"></span><span class="answer answer--open"></span></div>
      </li>
    </ol>
  </main>
</body>
</html>
```